Makers' Hollow - Landing page for small and large screen

Makers’ Hollow gives you the space you need to take your side project from idea to reality.

With three days of focused work, it’s a place for you iron out the details of your business idea away from the distractions of the city.

The full copy and structure is here:
https://www.makershollow.example.co.uk/landing

What it needs, a touch of colour.

Target Market(s)

25-35 working in digital industry, software developer, a UI or UX designer

Number of Pages Required

1 page

Font styles to use
Sans Serif

Colors
0292cd
33b8a4
86cfc6
fdf9cf
ec1f27

Requirements
Should not have
• gradients or too much images

```html
<!DOCTYPE html>
<html lang="en">
<head>
<meta charset="utf-8">
<title>Makers' Hollow</title>
<link href="https://fonts.googleapis.com/css2?family=Montserrat:wght@200;800&family=Questrial&display=swap" rel="stylesheet">
<style>
  :root {
    --blue: #0292cd;
    --teal: #33b8a4;
    --mint: #86cfc6;
    --cream: #fdf9cf;
    --paper: #fefcee;
    --red: #ec1f27;
    --ink: #1c1c1c;
    --white: #ffffff;
  }
  * { box-sizing: border-box; margin: 0; padding: 0; }
  html, body { width: 1152px; height: 1200px; overflow: hidden; }
  body { background: var(--paper); font-family: "Questrial", sans-serif; color: var(--ink); position: relative; }

  .hero { position: absolute; left: 0; top: 0; width: 1152px; height: 638px; overflow: hidden; }
  .hero-photo { position: absolute; inset: 0; background: linear-gradient(180deg, #3f3a36 0%, #58514b 55%, #6a6560 100%); }
  .hero-shade { position: absolute; inset: 0; background: rgba(20, 20, 20, 0.25); }

  .nav-links { position: absolute; left: 132px; top: 48px; display: flex; gap: 40px; list-style: none; }
  .nav-links a { color: var(--white); text-decoration: none; font-size: 14.5px; }

  .brand { position: absolute; left: 463px; top: 0; width: 227px; height: 141px; background: var(--cream); border-radius: 0 0 12px 12px; text-align: center; padding-top: 42px; }
  .brand-name { font-family: "Questrial", sans-serif; font-size: 27px; color: var(--blue); display: block; }
  .brand-tag { font-size: 9px; color: #555; display: block; margin-top: 8px; padding-left: 30px; }

  .btn { position: absolute; display: flex; align-items: center; justify-content: center; color: var(--white); text-decoration: none; font-size: 14px; border-radius: 2px; }
  .btn-join-top { left: 871px; top: 40px; width: 149px; height: 40px; background: var(--red); }
  .btn-video { left: 399px; top: 434px; width: 176px; height: 47px; border: 1px solid rgba(255,255,255,0.3); background: rgba(255,255,255,0.06); gap: 14px; }
  .btn-join { left: 592px; top: 434px; width: 160px; height: 47px; background: var(--red); }

  .hero-title { position: absolute; left: 0; top: 190px; width: 1152px; text-align: center; font-family: "Montserrat", sans-serif; font-weight: 800; font-size: 40px; line-height: 50px; color: var(--white); letter-spacing: -0.4px; }
  .hero-sub { position: absolute; left: 0; top: 354px; width: 1152px; text-align: center; font-family: "Montserrat", sans-serif; font-weight: 200; font-size: 40px; color: var(--white); letter-spacing: 0.3px; }
  .scroll-cue { position: absolute; left: 569px; top: 567px; }

  .offer-title { position: absolute; left: 0; top: 686px; width: 1152px; text-align: center; font-family: "Montserrat", sans-serif; font-weight: 800; font-size: 41px; color: var(--teal); }
  .offer-copy { position: absolute; left: 132px; top: 788px; width: 345px; font-size: 19px; line-height: 32px; letter-spacing: 0.4px; }
  .offer-visual { position: absolute; left: 573px; top: 786px; width: 445px; height: 414px; background: linear-gradient(180deg, #e6e6e4 0%, #dcd6d0 100%); }
</style>
</head>
<body>
  <header class="hero">
    <div class="hero-photo" role="img" aria-label="Photo of a person sitting in a large empty brick hall beneath a cluster of balloons"></div>
    <div class="hero-shade"></div>
    <ul class="nav-links">
      <li><a href="#why">Why Makers’ Hollow?</a></li>
      <li><a href="#offer">What you’ll get</a></li>
    </ul>
    <div class="brand">
      <span class="brand-name">Makers’ Hollow</span>
      <span class="brand-tag">Create. Connect. Collaborate</span>
    </div>
    <a class="btn btn-join-top" href="#join">JOIN US</a>
    <h1 class="hero-title">We give you the space you<br>need to take your side project<br>from idea to reality.</h1>
    <p class="hero-sub">create. connect. collaborate</p>
    <a class="btn btn-video" href="#video">
      <svg width="10" height="13" viewBox="0 0 10 13"><path d="M0 0 L10 6.5 L0 13 Z" fill="#fff"/></svg>
      Watch video
    </a>
    <a class="btn btn-join" href="#join">Join Us...</a>
    <svg class="scroll-cue" width="14" height="22" viewBox="0 0 14 22"><rect x="1" y="1" width="12" height="20" rx="6" fill="none" stroke="rgba(255,255,255,0.5)" stroke-width="1.5"/><rect x="6" y="5" width="2" height="4" rx="1" fill="rgba(255,255,255,0.7)"/></svg>
  </header>

  <main id="offer">
    <h2 class="offer-title">What we offer</h2>
    <div class="offer-copy">
      <p>Calling all creatives! Whether you’re a software developer, a UI or UX designer, a product creator or an artworker, you’ll know only too well that great work rarely materialises when you’re in the wrong environment.</p>
      <p>Phones buzzing. Emails pinging. Zuvachat calls incoming...distractions are everywhere – and they do nothing for your motivation.</p>
      <p>So, if you have a seed of a business idea and need to reclaim some focus, this is the place for you.</p>
    </div>
    <div class="offer-visual" role="img" aria-label="Illustration of a person with eyes closed whose thoughts scatter into small pixel squares"></div>
  </main>
</body>
</html>
```